Industry automation wholesale website

www.velqora.eu provides solutions for automation, building automation and digital signage.

Our products are rugged, reliable, energy saving and representative.

Scope of pages:
● welcome page
- scope of products
- applications, success stories and news
● category page
- short introduction
- sub categories
- product highlights
● product page
- short introduction
- about 3 to 4 pictures
- technical specifications: materials, dimensions
- price
- related products

Optional:
● contact page
- address
- contact form
● blog
- picture
- text
● logo
● favicon / apple touch icon

Conclusion:
● We need a professionally looking site
● Bright colors (e.g. white, grey, metalic colors, blue)

some pages we like:
http://www.brundafel.de/
http://www.korvimash.de/

Target Market(s)

Our target market is the industrial sector
● Target audience: engineering and IT professionals

Industry/Entity Type

Building

Requirements
Must have
• ● only use free available fonts e.g. Pellor Type Library (http://www.pellortype.com/webfonts)
Should not have
• ● sound
● flash

```html
<!DOCTYPE html>
<html lang="en">
<head>
<meta charset="utf-8">
<title>RS422 / RS485 Converter – velqora</title>
<link href="https://fonts.googleapis.com/css2?family=Arimo:wght@400;700&family=Open+Sans:wght@400;600&display=swap" rel="stylesheet">
<style>
:root{
  --accent-red:#d23a36;
  --brand-blue:#1f6f9a;
  --link-blue:#2f66b3;
  --nav-top:#3a6db2;
  --nav-bottom:#173f82;
  --text:#555;
  --muted:#8a8a8a;
  --rule:#d6d6d6;
  --panel:#f2f2f2;
  --white:#fff;
}
*{margin:0;padding:0;box-sizing:border-box}
html,body{width:1200px;height:1000px;overflow:hidden}
body{position:relative;background:#f4f5f7;font-family:"Arimo",Arial,sans-serif;color:var(--text)}
.top-strip{position:absolute;left:0;top:0;width:1200px;height:5px;background:var(--accent-red)}
.header-visual{position:absolute;left:0;top:5px;width:1200px;height:162px;
  background:linear-gradient(180deg,#eef1f6 0%,#e3e8f1 60%,#aebfe0 82%,#5c7fc4 100%)}
.side-visual{position:absolute;left:0;top:167px;width:52px;height:87px;
  background:linear-gradient(180deg,#6f8fd0,#c9d6ee)}
.brand{position:absolute;left:90px;top:26px;display:flex;align-items:center;gap:12px}
.brand-name{font-family:"Open Sans",Arial,sans-serif;font-size:62px;font-weight:400;color:var(--brand-blue);line-height:1}
.brand-mark{width:14px;height:14px;background:var(--brand-blue)}
.contact-bar{position:absolute;right:0;top:16px;display:flex;align-items:center;font-size:17px;color:#666}
.contact-bar .item{display:flex;align-items:center;gap:8px;padding:0 22px}
.contact-bar .item+.item{border-left:1px solid #c8c8c8}
.main-nav{position:absolute;left:52px;top:167px;width:1148px;height:45px;
  background:linear-gradient(180deg,var(--nav-top),var(--nav-bottom));display:flex}
.main-nav a{display:flex;align-items:center;justify-content:center;color:var(--white);
  text-decoration:none;font-family:"Open Sans",Arial,sans-serif;font-size:17px;font-weight:600;border-right:1px solid #0f2d63}
.nav-rule{position:absolute;left:52px;top:212px;width:1148px;height:4px;background:#c5c9cf}
.page{position:absolute;left:52px;top:216px;width:1148px;height:784px;background:var(--white)}
.page-title{position:absolute;left:29px;top:26px;width:808px;height:45px;border-bottom:1px solid #c9c9c9;
  font-family:"Open Sans",Arial,sans-serif;font-weight:400;font-size:25px;color:var(--link-blue);padding-left:28px}
.chev{position:absolute;width:8px;height:10px}
.page-title .chev{left:11px;top:9px}
.product-shot{position:absolute;left:29px;top:98px;width:207px;height:174px;border:1px solid #dcdcdc;padding:10px}
.product-shot .fill{width:100%;height:100%;background:radial-gradient(circle at 50% 48%,#5f86d6 0%,#8aa6dd 35%,#fff 68%)}
.intro{position:absolute;left:260px;top:98px;width:570px;font-size:16px;line-height:29px}
.intro a{color:var(--link-blue);text-decoration:none}
.intro .lead{margin-top:10px}
.features{list-style:none;margin-top:2px}
.features li{position:relative;padding-left:27px;line-height:29px}
.features li::before{content:"";position:absolute;left:10px;top:11px;width:6px;height:6px;background:#d77a72}
.sub-heading{position:absolute;left:253px;top:632px;width:270px;height:35px;padding-left:8px;
  background:linear-gradient(90deg,#ececec,#fff);font-family:"Open Sans",Arial,sans-serif;font-size:21px;line-height:35px;color:#555}
.sub-card{position:absolute;top:696px;width:170px;height:100px;border:1px solid #dcdcdc;border-bottom:none;padding:10px 10px 0}
.sub-card .fill{width:100%;height:100%}
.sidebar{position:absolute;left:885px;top:25px;width:263px}
.sidebar h2{height:36px;padding-left:13px;background:linear-gradient(90deg,#ececec,#fafafa);
  font-family:"Open Sans",Arial,sans-serif;font-weight:400;font-size:21px;line-height:36px;color:#444}
.cat{position:relative;height:47px;background:var(--panel);border-bottom:1px solid var(--white);
  padding-left:33px;font-size:17px;line-height:46px;color:var(--link-blue)}
.cat .chev{left:14px;top:17px}
.sidebar .cat.active{margin-top:8px}
.subcat{position:relative;height:47px;border-bottom:1px solid #d8d8d8;padding-left:49px;font-size:16px;line-height:47px;color:var(--muted);white-space:nowrap;overflow:hidden}
.subcat::before{content:"";position:absolute;left:34px;top:21px;width:6px;height:6px;background:#3d6ab4}
.subs{margin-bottom:5px}
</style>
</head>
<body>
<div class="top-strip"></div>
<div class="header-visual" role="img" aria-label="Industrial welding scene with flying sparks, in pale blue tones"></div>
<div class="side-visual" role="img" aria-label="Continuation of the blue sparks backdrop"></div>

<div class="brand"><span class="brand-name">velqora</span><span class="brand-mark"></span></div>

<div class="contact-bar">
  <div class="item">
    <svg width="15" height="15" viewBox="0 0 24 24"><path fill="#4f7aa5" d="M6.6 10.8c1.4 2.8 3.8 5.1 6.6 6.6l2.2-2.2c.3-.3.7-.4 1-.2 1.1.4 2.3.6 3.6.6.6 0 1 .4 1 1V20c0 .6-.4 1-1 1C10.6 21 3 13.4 3 4c0-.6.4-1 1-1h3.5c.6 0 1 .4 1 1 0 1.3.2 2.5.6 3.6.1.3 0 .7-.2 1l-2.3 2.2z"/></svg>
    <span>+49-211-5540-218</span>
  </div>
  <div class="item">
    <svg width="20" height="14" viewBox="0 0 20 14"><rect x="0.5" y="0.5" width="19" height="13" fill="#5d87b5"/><path d="M1 1l9 7 9-7" stroke="#fff" stroke-width="1.4" fill="none"/></svg>
    <span>info@velqora.eu</span>
  </div>
</div>

<nav class="main-nav">
  <a href="#" style="width:126px">Home</a>
  <a href="#" style="width:148px">Category</a>
  <a href="#" style="width:141px">Products</a>
  <a href="#" style="width:141px">Contact</a>
  <a href="#" style="width:109px">Blog</a>
  <a href="#" style="width:110px">Cart</a>
</nav>
<div class="nav-rule"></div>

<main class="page">
  <h1 class="page-title"><svg class="chev" viewBox="0 0 8 10"><path d="M0 0h3l5 5-5 5H0l5-5z" fill="#d23a36"/></svg>RS422 / RS485 Converter</h1>

  <div class="product-shot"><div class="fill" role="img" aria-label="Blue DIN-rail serial converter module with green terminal blocks"></div></div>

  <div class="intro">
    <p>Our ProlinkDAQ <a href="#">RS422 / RS485 converters</a>, RS422 / RS485 repeaters and RS485 Feldbus remote IO modules have been developed for professional use in the industry.</p>
    <p>The production line includes the converters RS232 RS422, USB RS422, RS232 RS485 and USB RS485, the repeaters RS422 and RS485, and serial IP converters.</p>
    <p class="lead">Features:</p>
    <ul class="features">
      <li>RS422/RS485 communication: up to 1200m</li>
      <li>Extended operating temperature: -25°C to +75°C</li>
      <li>Power input: +10V to +30V</li>
      <li>Isolation between input and output signal</li>
      <li>Automatic baudrate detection (no dip-switch)</li>
      <li>Automatically recognized whether a RS232 or a RS422 / RS485 Feldbus network has been connected</li>
      <li>Parameters and the direction of the transmission are recognized automa­tically</li>
      <li>Cap-rails and wall supporters included</li>
    </ul>
  </div>

  <h2 class="sub-heading">5 Sub Categories:</h2>
  <div class="sub-card" style="left:263px"><div class="fill" role="img" aria-label="Serial cable adapter with multiple connectors" style="background:linear-gradient(180deg,#fff 40%,#6d6d6d)"></div></div>
  <div class="sub-card" style="left:454px"><div class="fill" role="img" aria-label="Blue USB serial converter module" style="background:linear-gradient(180deg,#fff 20%,#4f83c7)"></div></div>
  <div class="sub-card" style="left:644px"><div class="fill" role="img" aria-label="Wireless serial converter with antenna" style="background:linear-gradient(180deg,#fff 25%,#6b97d3)"></div></div>

  <aside class="sidebar">
    <h2>Range Of Products</h2>
    <div class="cat active"><svg class="chev" viewBox="0 0 8 10"><path d="M0 0h3l5 5-5 5H0l5-5z" fill="#d23a36"/></svg>RS422 / RS485 Converter</div>
    <div class="subs">
      <div class="subcat">RS232 to RS422/RS485 Converter</div>
      <div class="subcat">RS232 USB Converter</div>
      <div class="subcat">RS422 / RS485 USB Converter</div>
      <div class="subcat">RS422 / RS485 Ethernet Converter</div>
      <div class="subcat">RS422 / RS485 WLan Converter</div>
    </div>
    <div class="cat"><svg class="chev" viewBox="0 0 8 10"><path d="M0 0h3l5 5-5 5H0l5-5z" fill="#d23a36"/></svg>RS422 / RS485 Repeater</div>
    <div class="cat"><svg class="chev" viewBox="0 0 8 10"><path d="M0 0h3l5 5-5 5H0l5-5z" fill="#d23a36"/></svg>RS485 Remote IO</div>
    <div class="cat"><svg class="chev" viewBox="0 0 8 10"><path d="M0 0h3l5 5-5 5H0l5-5z" fill="#d23a36"/></svg>RS485 Modbus IO</div>
    <div class="cat"><svg class="chev" viewBox="0 0 8 10"><path d="M0 0h3l5 5-5 5H0l5-5z" fill="#d23a36"/></svg>Embedded Systems</div>
    <div class="cat"><svg class="chev" viewBox="0 0 8 10"><path d="M0 0h3l5 5-5 5H0l5-5z" fill="#d23a36"/></svg>PCI-Series</div>
    <div class="cat"><svg class="chev" viewBox="0 0 8 10"><path d="M0 0h3l5 5-5 5H0l5-5z" fill="#d23a36"/></svg>PCI-Series</div>
  </aside>
</main>
</body>
</html>
```